Roofing Contractor website

I currently have a website. But I would like it redesigned. Here is my website:
www.brambletopshingle.co

I want to try and mimic the look of another website: www.vestapixelworks.com

For legal reasons I don’t want to copy it 100%, but I would like to copy it as much as possible because I like the look and simplicity of this website. We have similar colors. My company colors are black, red and white.

I am not very good at web design, but I am good enough to go into front page and change some text and images if the main design is already created for me. I am looking for someone to basically create 95% of this front page site for me, and I can go in and tweak some of the wording and images later.

My current website already has SEO work done. So I do not want to lose the work that is done already because I am currently ranked very well in my area. I just want the design of my site to change but not lose any seo rankings.

I attached some wording id like to replace from the vesta pixelworks website. But this is NOT complete. Just some notes I wrote down. We can get together to make this more complete later.

The most important things to me is that I do not lose SEO and the overall look and design is similar to vesta pixelworks website but its designed for my brambletop shingle website.

Coding

```html
<!DOCTYPE html>
<html lang="en">
<head>
<meta charset="utf-8">
<title>Brambletop Shingle – Roofing Contractor</title>
<link href="https://fonts.googleapis.com/css2?family=Jost:wght@400;500;600&family=Archivo:wght@600;700;800&display=swap" rel="stylesheet">
<style>
:root{
  --black:#000;
  --ink:#111;
  --white:#fff;
  --red:#e50914;
  --red-dark:#b00000;
  --grey:#555;
  --grey-soft:#6b6b6b;
  --teal:#2c6f75;
  --star:#ffe500;
  --panel:#1c1c1c;
}
*{margin:0;padding:0;box-sizing:border-box}
html,body{width:1200px;height:2958px;overflow:hidden;background:var(--white)}
body{position:relative;font-family:"Jost",sans-serif;color:var(--ink)}
.abs{position:absolute}
.display{font-family:"Archivo",sans-serif;font-weight:800}
.accent{color:var(--red)}

/* Reviews */
.reviews{left:0;top:0;width:1200px;height:471px;background:var(--black);color:var(--white)}
.review .avatar{width:101px;height:101px;border-radius:50%}
.review .name{font-weight:600;font-size:19px;line-height:1}
.review .date{font-size:15px;margin-top:4px}
.review .stars{color:var(--star);font-size:30px;letter-spacing:4px;margin-top:8px;line-height:1}
.review .text{font-size:15px;line-height:18.5px;width:390px}
.rating-badge{left:316px;top:271px;width:568px;height:135px;border:1px solid #555;border-radius:12px;background:var(--panel);text-align:center}
.rating-badge .title{font-family:"Jost",sans-serif;font-weight:600;font-size:50px;color:var(--red);margin-top:12px;line-height:1.1}
.rating-badge .stars{color:var(--star);font-size:32px;letter-spacing:4px;margin-top:6px}

/* FAQ */
.faq-title{left:0;width:1145px;top:556px;text-align:center;font-size:37px;letter-spacing:.2px}
.faq-q{font-size:19px;color:#333;width:470px}
.faq-a{font-size:15px;line-height:20px;color:var(--grey-soft);width:425px}
.faq-icon{width:22px;height:22px}

/* Blog */
.blog-title{left:69px;top:1190px;font-size:38px;line-height:44px}
.btn{display:flex;height:48px;border-radius:8px;overflow:hidden;font-family:"Archivo",sans-serif;font-weight:700;font-size:19px}
.btn .label{display:flex;align-items:center;justify-content:center}
.btn .arrow{display:flex;align-items:center;justify-content:center}
.blog-btn{left:866px;top:1254px;width:240px;background:var(--red-dark);color:var(--white)}
.blog-btn .label{width:183px}
.blog-btn .arrow{flex:1;background:var(--red)}
.photo{border-radius:12px}

/* CTA */
.cta-band{left:0;top:2358px;width:1200px;height:600px;background:var(--black)}
.cta-card{left:118px;top:2169px;width:963px;height:326px;border-radius:16px;background:var(--black);overflow:hidden;box-shadow:0 3px 0 #777}
.cta-photo{left:0;top:0;width:490px;height:326px;background:linear-gradient(160deg,#3b6fb4 0%,#9fb9dc 45%,#4d6f9a 75%,#1f2f48 100%)}
.cta-fade{left:380px;top:0;width:120px;height:326px;background:linear-gradient(90deg,rgba(0,0,0,0),#000)}
.cta-title{left:482px;top:45px;font-size:37px;line-height:43px;color:var(--white)}
.cta-quote{left:482px;top:165px;width:415px;font-size:14px;line-height:15px;color:var(--white)}
.cta-btn{left:586px;top:244px;width:240px;background:var(--white);color:var(--black)}
.cta-btn .label{width:183px}
.cta-btn .arrow{flex:1;background:var(--red)}

/* Footer */
.footer{color:var(--white)}
.brand{left:36px;top:2575px;width:130px;text-align:center;font-family:"Archivo",sans-serif;font-weight:800;font-size:16px;line-height:18px;color:var(--red);text-transform:uppercase}
.brand .dot{width:40px;height:40px;border-radius:50%;background:var(--red);margin:0 auto 8px}
.info{display:flex;align-items:center;gap:30px}
.info .small{font-size:15px;color:#ccc}
.info .big{font-size:20px}
.footer-head{font-family:"Archivo",sans-serif;font-weight:800;font-size:20px;letter-spacing:.5px}
.footer-list{list-style:none;font-size:19px;color:#ddd}
.footer-list li{height:38.5px}
.socials{display:flex;gap:11px}
.socials span{width:28px;height:28px;border:1.5px solid #aaa;border-radius:50%}
.rule{left:0;top:2866px;width:1200px;height:1px;background:#444}
.copyright{left:626px;top:2894px;font-size:17px;color:#999;letter-spacing:.3px}
</style>
</head>
<body>

<section class="reviews abs">
  <article class="review">
    <div class="avatar abs" style="left:121px;top:16px;background:linear-gradient(135deg,#c9a36a,#6f5a3a)" role="img" aria-label="Reviewer portrait"></div>
    <div class="abs" style="left:241px;top:18px">
      <div class="name">Marla Quinlan</div>
      <div class="date">January 26, 2024</div>
      <div class="stars">★★★★★</div>
    </div>
    <p class="text abs" style="left:121px;top:138px">Dale has done our Christmas lights the last few years. He's also done some roof work for us. Each time it has been spot on!! Great service and professionalism! Highly recommend using this company!</p>
  </article>
  <article class="review">
    <div class="avatar abs" style="left:648px;top:16px;background:linear-gradient(135deg,#c8a58a,#3a2e28)" role="img" aria-label="Reviewer portrait"></div>
    <div class="abs" style="left:785px;top:18px">
      <div class="name">Marla Quinlan</div>
      <div class="date">January 26, 2024</div>
      <div class="stars">★★★★★</div>
    </div>
    <p class="text abs" style="left:664px;top:138px">Dale has done our Christmas lights the last few years. He's also done some roof work for us. Each time it has been spot on!! Great service and professionalism! Highly recommend using this company!</p>
  </article>
  <div class="rating-badge abs">
    <div class="title">Verified 5 Star</div>
    <div class="stars">★★★★★</div>
  </div>
</section>

<section class="faq">
  <h2 class="faq-title abs display">COMMONLY <span class="accent">&nbsp;ASKED QUESTIONS</span></h2>

  <div class="faq-q abs" style="left:48px;top:704px">The Solarix &nbsp;what you need to konw?</div>
  <svg class="faq-icon abs" style="left:540px;top:709px" viewBox="0 0 22 22"><line x1="0" y1="11" x2="22" y2="11" stroke="#2c6f75" stroke-width="1.5"/></svg>
  <p class="faq-a abs" style="left:51px;top:761px">Lorem ipsum dolor sit amet, consectetur adipiscing elit. Cras sed nisi tempor, congue tellus a, tempus sapien. Lorem ipsum dolor sit amet, consectetur adipiscing elit. Pellentesque bibendum ornare facilisis. Lorem ipsum dolor sit amet, consectetur adipiscing elit. Donec non tincidunt orci, vitae sagittis mauris.</p>
  <div class="faq-q abs" style="left:48px;top:889px">Donec rutrum, ligula sit amet blandit scelerisque</div>
  <div class="faq-q abs" style="left:48px;top:951px">Sed et dignissim magna. Duis ac augue interdum</div>
  <div class="faq-q abs" style="left:48px;top:1013px">Morbi nec magna at risus malesuada laoreet.</div>
  <svg class="faq-icon abs" style="left:540px;top:893px" viewBox="0 0 22 22"><path d="M0 11H22M11 0V22" stroke="#2c6f75" stroke-width="1.5"/></svg>
  <svg class="faq-icon abs" style="left:540px;top:952px" viewBox="0 0 22 22"><path d="M0 11H22M11 0V22" stroke="#2c6f75" stroke-width="1.5"/></svg>
  <svg class="faq-icon abs" style="left:540px;top:1015px" viewBox="0 0 22 22"><path d="M0 11H22M11 0V22" stroke="#2c6f75" stroke-width="1.5"/></svg>

  <div class="faq-q abs" style="left:633px;top:704px">The Solarix &nbsp;what you need to konw?</div>
  <svg class="faq-icon abs" style="left:1121px;top:709px" viewBox="0 0 22 22"><line x1="0" y1="11" x2="22" y2="11" stroke="#2c6f75" stroke-width="1.5"/></svg>
  <p class="faq-a abs" style="left:634px;top:761px">Lorem ipsum dolor sit amet, consectetur adipiscing elit. Cras sed nisi tempor, congue tellus a, tempus sapien. Lorem ipsum dolor sit amet, consectetur adipiscing elit. Pellentesque bibendum ornare facilisis. Lorem ipsum dolor sit amet, consectetur adipiscing elit. Donec non tincidunt orci, vitae sagittis mauris.</p>
  <div class="faq-q abs" style="left:633px;top:889px">Donec rutrum, ligula sit amet blandit scelerisque</div>
  <div class="faq-q abs" style="left:633px;top:951px">Sed et dignissim magna. Duis ac augue interdum</div>
  <div class="faq-q abs" style="left:633px;top:1015px">Morbi nec magna at risus malesuada laoreet.</div>
  <svg class="faq-icon abs" style="left:1121px;top:893px" viewBox="0 0 22 22"><path d="M0 11H22M11 0V22" stroke="#2c6f75" stroke-width="1.5"/></svg>
  <svg class="faq-icon abs" style="left:1121px;top:952px" viewBox="0 0 22 22"><path d="M0 11H22M11 0V22" stroke="#2c6f75" stroke-width="1.5"/></svg>
  <svg class="faq-icon abs" style="left:1121px;top:1015px" viewBox="0 0 22 22"><path d="M0 11H22M11 0V22" stroke="#2c6f75" stroke-width="1.5"/></svg>
</section>

<section class="blog">
  <h2 class="blog-title abs display">CHECKOUT<br>OUR &nbsp;<span class="accent">BLOG ARTICLES</span></h2>
  <a class="blog-btn btn abs"><span class="label">View More Blogs</span><span class="arrow"><svg width="24" height="14" viewBox="0 0 24 14"><path d="M1 7H22M16 1L22 7L16 13" fill="none" stroke="#fff" stroke-width="2"/></svg></span></a>
  <div class="photo abs" style="left:26px;top:1333px;width:464px;height:689px;background:linear-gradient(160deg,#8a8a8a,#4a4a4a 55%,#2f2f2f)" role="img" aria-label="Roofer with safety harness working on shingles"></div>
  <div class="photo abs" style="left:518px;top:1333px;width:303px;height:325px;background:linear-gradient(180deg,#c9dff0,#e8e0d0 55%,#8a8a7a)" role="img" aria-label="Contractors reviewing plans outside a house"></div>
  <div class="photo abs" style="left:870px;top:1333px;width:304px;height:325px;background:linear-gradient(180deg,#c6cfd0,#e8c07a 55%,#8a7560)" role="img" aria-label="Two roofers installing a roof at sunset"></div>
  <div class="photo abs" style="left:518px;top:1720px;width:656px;height:302px;background:linear-gradient(180deg,#a9c3dc,#5e6466 45%,#3d5a2e 100%)" role="img" aria-label="Two-storey house with new shingle roof"></div>
</section>

<section class="cta">
  <div class="cta-band abs"></div>
  <div class="cta-card abs">
    <div class="cta-photo abs" role="img" aria-label="Skydivers in free fall above the clouds"></div>
    <div class="cta-fade abs"></div>
    <svg class="abs" style="left:600px;top:0" width="363" height="326" viewBox="0 0 363 326"><g stroke="#2a2a2a" stroke-width="1.5"><line x1="363" y1="20" x2="80" y2="326"/><line x1="363" y1="70" x2="125" y2="326"/><line x1="363" y1="120" x2="170" y2="326"/><line x1="363" y1="170" x2="215" y2="326"/><line x1="363" y1="220" x2="260" y2="326"/><line x1="340" y1="0" x2="40" y2="326"/></g></svg>
    <h2 class="cta-title abs display">READY TO <span class="accent">TAKE A<br>LEAP</span>?</h2>
    <p class="cta-quote abs">“We know what it takes to help get home service businesses more leads from online search. Even if we're not the right fit, we'll get you where you need to go.”</p>
    <a class="cta-btn btn abs"><span class="label">Give Us a Call</span><span class="arrow"><svg width="24" height="14" viewBox="0 0 24 14"><path d="M1 7H22M16 1L22 7L16 13" fill="none" stroke="#fff" stroke-width="2"/></svg></span></a>
  </div>
</section>

<footer class="footer">
  <div class="brand abs"><div class="dot"></div>Brambletop Shingle</div>

  <div class="info abs" style="left:36px;top:2695px">
    <svg width="38" height="44" viewBox="0 0 38 44"><path d="M8 4C3 7 2 14 7 24s13 17 19 16c3 0 5-3 5-5l-6-6-5 3c-3-2-7-7-8-11l4-4-5-8z" fill="none" stroke="#fff" stroke-width="2"/><path d="M22 8a9 9 0 0 1 8 8M22 2a15 15 0 0 1 14 14" fill="none" stroke="#fff" stroke-width="2"/></svg>
    <div><div class="small">Give Us a Call:</div><div class="big">555-014-2290</div></div>
  </div>
  <div class="info abs" style="left:38px;top:2778px">
    <svg width="34" height="50" viewBox="0 0 34 50"><path d="M17 48C5 30 2 24 2 17a15 15 0 0 1 30 0c0 7-3 13-15 31z" fill="none" stroke="#fff" stroke-width="2"/><circle cx="17" cy="17" r="6" fill="none" stroke="#fff" stroke-width="2"/></svg>
    <div><div class="small">Visit Our Office:</div><div class="big">Cedar Hollow, Texas</div></div>
  </div>

  <h3 class="footer-head abs" style="left:393px;top:2572px">SERVICES</h3>
  <ul class="footer-list abs" style="left:393px;top:2623px">
    <li>Roof Replacements</li><li>Roof Repairs</li><li>Gutters</li><li>Christmas Light</li><li>Installation</li><li>Fencing</li>
  </ul>

  <h3 class="footer-head abs" style="left:688px;top:2574px">QUICK LINK</h3>
  <ul class="footer-list abs" style="left:688px;top:2612px">
    <li>Contact us</li><li>Resources</li><li>Sitemap</li><li>FAQS</li>
  </ul>

  <h3 class="footer-head abs" style="left:920px;top:2577px">CONTACT</h3>
  <div class="abs" style="left:920px;top:2622px;font-size:19px;color:#ddd">Email</div>
  <div class="abs" style="left:920px;top:2656px;font-size:15px">info@brambletopshingle.co</div>
  <div class="abs" style="left:920px;top:2716px;font-size:19px;color:#ddd">Connect with us</div>
  <div class="socials abs" style="left:920px;top:2757px"><span></span><span></span><span></span><span></span></div>

  <div class="rule abs"></div>
  <p class="copyright abs">© 2025 Brambletop Shingle | All rights reserved.</p>
</footer>

</body>
</html>
```